I need a business card design for my new chiropractic business.It is chiropractic that addresses the whole body, is natural, done by hand, will reduce pain, increase vitality, reduce stress. It is safe and suitable for all ages.I am a Varrowdale chiropractor and they have a particular logo see VCA.example.co.uk. I would like Fernleaf Chiropractic and Varrowdale to feature if possible. Purple colours and tones please.

Target Market(s)

People who are interested in their health and being empowered to take responsibility for their well being.

Industry/Entity Type

Business

Contact Information for Business Card

My name, Marnie Castell
RPB Reg No 07213
Tel No 07900 118457

Font styles to use
Sans Serif
Other font styles liked:
• ITALIC?

Colors
b768aa
886aae
a6459a
6c459b
ffffff
e567a6

Requirements
Must have
• graphic to represent healing by hand and increase in well being. by restoring spinal and nervous system function.
• Professional and clear layout and information
• Some or all of the words above in project description
• Varrowdale logo (from varrowdalechiropractic.example.org).
Nice to have
• Transformative theme- body- from pain to freedom of motion. A more fully integrated
• System, better functioning and connections.
• Clear layout and message
Should not have
• Must not look tacky

```html
<!DOCTYPE html>
<html lang="en">
<head>
<meta charset="utf-8">
<title>Varrowdale Chiropractic – Business Card</title>
<link rel="stylesheet" href="https://fonts.googleapis.com/css2?family=Arimo:ital,wght@0,400;0,700;1,400&display=swap">
<style>
  :root {
    --page-bg: #eeedf0;
    --card-deep: #1f1128;
    --card-plum: #3b2050;
    --card-violet: #6c459b;
    --card-lilac: #886aae;
    --card-orchid: #b768aa;
    --glow-warm: #f6b25a;
    --glow-core: #ffe7b8;
    --panel-dark: rgba(20, 10, 26, 0.72);
    --text-light: #ffffff;
    --text-soft: #d9cce6;
  }
  * { margin: 0; padding: 0; box-sizing: border-box; }
  html, body {
    width: 1200px; height: 719px; overflow: hidden;
    background: var(--page-bg);
    font-family: "Arimo", Arial, sans-serif;
  }
  .business-card {
    position: absolute; left: 75px; top: 60px;
    width: 1050px; height: 600px;
    background: var(--card-deep);
    overflow: hidden;
    box-shadow: 0 6px 18px rgba(0,0,0,0.18);
  }
  .hero-image {
    position: absolute; left: 0; top: 0; width: 100%; height: 84%;
    background:
      radial-gradient(ellipse 14% 20% at 66% 38%, var(--glow-core) 0%, var(--glow-warm) 35%, rgba(246,178,90,0) 100%),
      radial-gradient(ellipse 26% 40% at 66% 40%, rgba(183,104,170,0.55) 0%, rgba(183,104,170,0) 100%),
      radial-gradient(ellipse 70% 80% at 50% 50%, var(--card-violet) 0%, var(--card-plum) 55%, var(--card-deep) 100%);
  }
  .brand-panel {
    position: absolute; left: 0; top: 50px;
    width: 390px; height: 128px;
    background: var(--panel-dark);
    padding: 20px 0 0 30px;
  }
  .brand-name {
    display: flex; align-items: center; gap: 12px;
    font-weight: 700; font-size: 42px; letter-spacing: 0.5px;
    color: var(--text-light); line-height: 1;
  }
  .brand-mark {
    width: 26px; height: 26px; background: var(--card-orchid);
  }
  .brand-sub {
    margin-top: 6px; margin-left: 38px;
    font-size: 11px; letter-spacing: 2px; color: var(--text-soft);
  }
  .brand-line {
    margin-top: 8px; margin-left: 38px;
    font-size: 16px; color: var(--text-light);
  }
  .holder {
    position: absolute; left: 58px; top: 245px;
    color: var(--text-light);
  }
  .holder-name { font-weight: 700; font-size: 38px; }
  .holder-role { margin-top: 10px; margin-left: 70px; font-size: 20px; }
  .contact-panel {
    position: absolute; right: 0; top: 350px;
    width: 330px; height: 106px;
    background: var(--panel-dark);
    padding: 22px 0 0 24px;
    color: var(--text-light);
    font-weight: 700; font-size: 18px; line-height: 32px;
  }
  .contact-label { display: inline-block; width: 134px; }
  .accent-band {
    position: absolute; left: 0; top: 84%; width: 100%; height: 6%;
    background: linear-gradient(90deg, var(--card-violet), var(--card-lilac) 55%, var(--card-violet));
  }
  .base-band {
    position: absolute; left: 0; top: 90%; width: 100%; height: 10%;
    background: var(--card-deep);
  }
</style>
</head>
<body>
  <article class="business-card">
    <div class="hero-image" role="img" aria-label="Photograph of cupped hands holding a warm glowing light over purple leaves"></div>

    <header class="brand-panel">
      <div class="brand-name"><span class="brand-mark"></span>Varrowdale</div>
      <div class="brand-sub">CHIROPRACTIC</div>
      <div class="brand-line">natural care for the whole body</div>
    </header>

    <section class="holder">
      <div class="holder-name">Marnie Castell</div>
      <div class="holder-role">Manager</div>
    </section>

    <section class="contact-panel">
      <div class="contact-row"><span class="contact-label">RPB Reg No :</span>07213</div>
      <div class="contact-row"><span class="contact-label">Tel No :</span>07900 118457</div>
    </section>

    <div class="accent-band"></div>
    <div class="base-band"></div>
  </article>
</body>
</html>
```